Design a Travel and Tourism website

We would like a freelancer to design a website that is essentially easy to use and navigate database providing local information for Travelers about destination countries.

We proposed website would discuss different rates, fees, visa requirement, resort locations, cheap flights, etc. This website should be elegant and modern. Our business name is mirdalon.
Some reference websites are plendavix.ca, gosthandiverquo.com,
There should be a forum in the website where travell\ers discuss about their first hand tranvel experience to such destinations.

```html
<!DOCTYPE html>
<html lang="en">
<head>
<meta charset="utf-8">
<title>Mirdalon – Travel &amp; Tourism</title>
<link href="https://fonts.googleapis.com/css2?family=Montserrat:wght@400;600;700&family=Open+Sans:wght@400;600;700&family=Great+Vibes&display=swap" rel="stylesheet">
<style>
:root{
  --navy:#1c2b5f;
  --navy-dark:#121d45;
  --blue:#1b7fd0;
  --blue-deep:#135fa8;
  --gold:#b59a5a;
  --gold-light:#c9ae6d;
  --grey-bg:#f0f0f0;
  --text:#333a4a;
  --muted:#7a7f8c;
  --line:#e2e2e2;
  --white:#fff;
}
*{box-sizing:border-box;margin:0;padding:0}
html,body{width:1200px;height:3243px;overflow:hidden}
body{font-family:"Open Sans",sans-serif;color:var(--text);background:var(--white);position:relative}
.abs{position:absolute}
.heading{font-family:"Montserrat",sans-serif;font-weight:700;color:var(--navy);text-align:center;letter-spacing:1px}
.subtabs{font-family:"Montserrat",sans-serif;font-size:10px;font-weight:700;text-align:center;letter-spacing:.5px}
.subtabs span{margin:0 8px}
.subtabs i{font-style:normal;color:var(--gold)}

/* top bar */
.topbar{top:0;left:0;width:1200px;height:22px;background:var(--navy-dark)}
.topbar .socials{left:143px;top:4px;display:flex;gap:4px}
.dot{width:14px;height:14px;border-radius:50%;background:#5b6a9a}
.topbar .account{right:143px;top:5px;display:flex;gap:18px;font-family:"Montserrat",sans-serif;font-size:9px;font-weight:600;color:#c9cfe4}
.navbar{top:22px;left:0;width:1200px;height:38px;background:var(--blue)}
.navbar a{position:absolute;top:0;height:38px;line-height:38px;font-family:"Montserrat",sans-serif;font-weight:700;font-size:11.5px;color:var(--white);text-decoration:none;letter-spacing:.5px}
.navbar a.active{background:var(--gold);padding:0 18px}
.logo-tab{left:515px;top:0;width:168px;height:90px;background:var(--white);border-radius:0 0 22px 22px;display:flex;align-items:center;justify-content:center;box-shadow:0 2px 6px rgba(0,0,0,.15)}
.brand{font-family:"Montserrat",sans-serif;font-weight:700;color:var(--navy);font-size:26px}

/* hero */
.hero{top:60px;left:0;width:1200px;height:351px;background:linear-gradient(180deg,#5d7fa8 0%,#3e5e4c 45%,#2b5a84 75%,#18408a 100%)}
.hero-title{left:250px;top:128px;font-family:"Great Vibes",cursive;color:var(--white);font-size:52px;line-height:54px;text-align:center}
.badge{left:742px;top:147px;width:194px;height:194px;border-radius:50%;background:var(--navy);border:6px solid var(--gold);display:flex;flex-direction:column;align-items:center;justify-content:center;color:var(--white);text-align:center}
.badge b{font-family:"Montserrat",sans-serif;font-size:21px;line-height:22px}
.badge small{font-size:11px;margin-top:8px}
.badge small em{font-style:normal;font-weight:700;color:var(--gold-light);font-size:18px}
.badge .brand{font-size:14px;color:var(--white);margin-top:8px}
.dots{left:588px;top:393px;display:flex;gap:6px}
.dots span{width:6px;height:6px;border-radius:50%;background:rgba(255,255,255,.7)}

/* search */
.search{top:411px;left:0;width:1200px;height:212px;background:var(--navy)}
.tab{position:absolute;top:36px;height:24px;line-height:24px;text-align:center;background:var(--navy-dark);color:var(--white);font-family:"Montserrat",sans-serif;font-weight:600;font-size:10px}
.tab.on{background:var(--gold)}
.field-label{position:absolute;top:74px;font-family:"Montserrat",sans-serif;font-weight:700;font-size:8px;color:var(--white)}
.field{position:absolute;top:88px;height:33px;background:var(--white);border-radius:2px;font-size:10px;color:#9aa0ad;line-height:33px;padding-left:24px}
.field svg{position:absolute;left:8px;top:10px}
.field.select{padding-left:10px;color:var(--text)}
.field.select:after{content:"";position:absolute;right:10px;top:12px;width:6px;height:6px;border-right:2px solid var(--text);border-bottom:2px solid var(--text);transform:rotate(45deg)}
.addcar{left:457px;top:152px;font-family:"Montserrat",sans-serif;font-size:10px;font-weight:600;color:var(--white);display:flex;align-items:center;gap:8px}
.addcar span{width:11px;height:11px;background:var(--white)}
.btn{position:absolute;height:33px;line-height:33px;text-align:center;background:var(--blue);color:var(--white);font-family:"Montserrat",sans-serif;font-weight:700;font-size:11px;border-radius:2px}

/* destinations */
.destinations{top:623px;left:0;width:1200px;height:614px}
.tile{position:absolute;box-shadow:0 2px 6px rgba(0,0,0,.25)}
.tile:after{content:"";position:absolute;inset:10px;border:1px solid rgba(255,255,255,.7)}
.tile .cap{position:absolute;left:20px;bottom:20px;color:var(--white);font-weight:600;font-size:15px}
.tile.feature{display:flex;flex-direction:column;align-items:center;justify-content:center;color:var(--white);text-align:center;background:linear-gradient(135deg,#2d6fd0,#17468f)}
.tile.feature h3{font-family:"Montserrat",sans-serif;font-size:26px;font-weight:600;margin-bottom:6px}
.tile.feature p{font-size:12px;line-height:17px;width:300px}

/* hotels */
.hotels{top:1237px;left:0;width:1200px;height:456px;background:linear-gradient(180deg,#1e86d6,#1570c0)}
.hotels .heading,.hotels .subtabs{color:var(--white)}
.hotel-img{position:absolute;top:153px;width:289px;height:188px;box-shadow:0 3px 8px rgba(0,0,0,.3)}
.hotel-img:after{content:"";position:absolute;inset:9px;border:1px solid rgba(255,255,255,.7)}
.hotel-info{position:absolute;top:350px;color:var(--white)}
.hotel-info b{display:block;font-size:13px;font-weight:600}
.hotel-info span{display:block;font-size:10px;color:#a9cff2;margin-top:2px}
.hotel-info i{display:block;font-style:normal;color:#f4c542;font-size:11px;letter-spacing:2px;margin-top:3px}

/* forum */
.forum{top:1693px;left:0;width:1200px;height:620px;background:var(--grey-bg)}
.forum .tagline{color:var(--gold);font-family:"Montserrat",sans-serif;font-weight:600;font-size:9.5px;text-align:center}
.table{left:143px;top:134px;width:914px;background:var(--white);border:1px solid var(--line)}
.thead{height:37px;background:var(--gold);color:var(--white);font-family:"Montserrat",sans-serif;font-weight:600;font-size:9.5px;position:relative}
.row{height:65.6px;border-top:1px solid var(--line);position:relative}
.c1{position:absolute;left:21px}
.c2{position:absolute;left:547px}
.c3{position:absolute;right:21px;text-align:right}
.thead .c1,.thead .c2,.thead .c3{top:13px}
.row .c1{top:16px}
.row .c1 b{display:block;color:var(--gold);font-size:12.5px;font-weight:600}
.row .c1 small{display:block;font-size:9.5px;margin-top:3px}
.row .c2{top:18px;font-size:9.5px}
.row .c3{top:18px;font-size:9.5px;line-height:14px}
.row .c3 em{font-style:normal;color:var(--gold)}

/* newsletter */
.newsletter{top:2313px;left:0;width:1200px;height:173px;background:linear-gradient(90deg,#1a70c2,#1f85d4 60%,#1668b3)}
.newsletter .heading{color:var(--white);font-size:19px}
.newsletter .sub{color:var(--white);font-family:"Montserrat",sans-serif;font-weight:600;font-size:9.5px;text-align:center}
.email{left:383px;top:93px;width:339px;height:35px;background:var(--white);font-size:10px;color:#9aa0ad;line-height:35px;padding-left:32px}
.email svg{position:absolute;left:10px;top:12px}
.submit{left:726px;top:93px;width:91px;height:35px;line-height:35px;background:var(--gold);color:var(--white);font-family:"Montserrat",sans-serif;font-weight:700;font-size:11px;text-align:center}

/* popular links */
.links{top:2486px;left:0;width:1200px;height:422px}
.link{position:absolute;width:290px;height:50px;border:1px solid #dcdcdc;clip-path:polygon(0 0,94% 0,100% 50%,94% 100%,0 100%);background:var(--white);display:flex;align-items:center;padding-left:18px;gap:14px;font-size:13.5px;color:var(--text)}
.link-frame{position:absolute;width:290px;height:50px}
.link-frame svg.edge{position:absolute;inset:0}

/* footer */
.footer{top:2908px;left:0;width:1200px;height:335px;background:linear-gradient(180deg,#ffffff 0%,#eef4fb 30%,#9cc3e6 70%,#3d6fb4 85%,#1c2b5f 100%)}
.footer .brand{position:absolute;left:0;width:1200px;text-align:center;top:60px;font-size:24px}
.footer .socials{position:absolute;left:572px;top:110px;display:flex;gap:5px}
.footer .socials span{width:24px;height:24px;border-radius:50%;background:#3a3f4b}
.footer nav{position:absolute;top:154px;left:0;width:1200px;text-align:center;font-family:"Montserrat",sans-serif;font-weight:700;font-size:10px;color:var(--navy)}
.footer nav span{margin:0 10px}
.footer .copy{position:absolute;top:173px;left:0;width:1200px;text-align:center;font-size:9.5px;color:var(--text)}
</style>
</head>
<body>

<header>
  <div class="abs topbar">
    <div class="abs socials"><span class="dot"></span><span class="dot"></span><span class="dot"></span></div>
    <div class="abs account"><span>ACCOUNT ▾</span><span>MY TRIPS</span><span>SUPPORT ▾</span></div>
  </div>
  <nav class="abs navbar">
    <a class="active" style="left:143px">HOME</a>
    <a style="left:238px">HOLIDAYS</a>
    <a style="left:339px">FLIGHTS</a>
    <a style="left:432px">HOTELS</a>
    <a style="left:728px">CARS</a>
    <a style="left:802px">DEALS</a>
    <a style="left:882px">INSURANCE</a>
    <a style="left:992px">FORUM</a>
  </nav>
  <div class="abs logo-tab"><span class="brand">Mirdalon</span></div>
</header>

<section class="abs hero" role="img" aria-label="Photo of green mountain ridges above a blue ocean coastline">
  <h1 class="abs hero-title" style="top:68px">Start Your Dream<br>Holidays Right Here</h1>
  <div class="abs badge" style="top:87px">
    <b>HAWAII<br>BEACHES</b>
    <small>From <em>$500</em> per person</small>
    <span class="brand">Mirdalon</span>
  </div>
  <div class="abs dots" style="top:333px"><span></span><span></span><span></span></div>
</section>

<section class="abs search">
  <div class="tab on" style="left:298px;width:111px">FLIGHT &amp; HOTEL</div>
  <div class="tab" style="left:424px;width:73px">HOLIDAYS</div>
  <div class="tab" style="left:508px;width:63px">FLIGHTS</div>
  <div class="tab" style="left:582px;width:60px">HOTELS</div>
  <div class="tab" style="left:657px;width:56px">CARS</div>
  <div class="tab" style="left:729px;width:86px">INSURANCE</div>
  <div class="tab" style="left:830px;width:74px">EXTRAS</div>

  <span class="field-label" style="left:143px">FLYING FROM</span>
  <span class="field-label" style="left:374px">FLYING TO</span>
  <span class="field-label" style="left:605px">DEPARTING</span>
  <span class="field-label" style="left:729px">RETURNING</span>
  <span class="field-label" style="left:854px">ROOMS</span>
  <span class="field-label" style="left:910px">ADULTS (18+)</span>
  <span class="field-label" style="left:981px">CHILDREN (0-17)</span>

  <div class="field" style="left:143px;width:225px"><svg width="9" height="12" viewBox="0 0 9 12"><path d="M4.5 0A4.5 4.5 0 0 0 0 4.5C0 8 4.5 12 4.5 12S9 8 9 4.5A4.5 4.5 0 0 0 4.5 0Zm0 6.3a1.8 1.8 0 1 1 0-3.6 1.8 1.8 0 0 1 0 3.6Z" fill="#9aa0ad"/></svg>City or Airport</div>
  <div class="field" style="left:374px;width:225px"><svg width="9" height="12" viewBox="0 0 9 12"><path d="M4.5 0A4.5 4.5 0 0 0 0 4.5C0 8 4.5 12 4.5 12S9 8 9 4.5A4.5 4.5 0 0 0 4.5 0Zm0 6.3a1.8 1.8 0 1 1 0-3.6 1.8 1.8 0 0 1 0 3.6Z" fill="#9aa0ad"/></svg>City or Airport</div>
  <div class="field" style="left:605px;width:117px"><svg width="12" height="12" viewBox="0 0 12 12"><rect x=".5" y="1.5" width="11" height="10" fill="none" stroke="#9aa0ad"/><rect x=".5" y="1.5" width="11" height="3" fill="#9aa0ad"/></svg>dd/mm/yyyy</div>
  <div class="field" style="left:729px;width:119px"><svg width="12" height="12" viewBox="0 0 12 12"><rect x=".5" y="1.5" width="11" height="10" fill="none" stroke="#9aa0ad"/><rect x=".5" y="1.5" width="11" height="3" fill="#9aa0ad"/></svg>dd/mm/yyyy</div>
  <div class="field select" style="left:854px;width:50px">1</div>
  <div class="field select" style="left:910px;width:65px">2</div>
  <div class="field select" style="left:981px;width:76px">0</div>

  <div class="abs addcar"><span></span>ADD A CAR</div>
  <div class="btn" style="left:551px;top:142px;width:95px">SEARCH</div>
</section>

<section class="abs destinations">
  <h2 class="heading abs" style="top:50px;width:1200px;font-size:26px">DESTINATIONS</h2>
  <div class="subtabs abs" style="top:96px;width:1200px"><span style="color:var(--blue)">TOP DESTINATIONS</span><i>|</i><span style="color:var(--gold)">FEATURED DESTINATIONS</span><i>|</i><span style="color:var(--gold)">POPULAR DESTINATIONS</span></div>

  <div class="tile" style="left:143px;top:147px;width:218px;height:406px;background:linear-gradient(160deg,#8aa3c4,#8a4a36 60%,#3c3b48)" role="img" aria-label="Photo of New York skyscrapers"><span class="cap">New York</span></div>
  <div class="tile feature" style="left:376px;top:147px;width:446px;height:194px">
    <h3>Bangkok</h3>
    <p>Lorem ipsum dolor sit amet, consectetur adipiscing elit, do eiusmod tempor incididunt ut labore.</p>
  </div>
  <div class="tile" style="left:376px;top:356px;width:446px;height:197px;background:linear-gradient(180deg,#5b6fa8,#d98048 55%,#4a2a3c)" role="img" aria-label="Photo of the Las Vegas welcome sign at sunset"><span class="cap">Las Vegas</span></div>
  <div class="tile" style="left:839px;top:147px;width:218px;height:406px;background:linear-gradient(180deg,#9fb6cf,#7a6650 55%,#3f5d7a)" role="img" aria-label="Photo of a hula dancer on a Hawaiian beach"><span class="cap">Hawaii</span></div>
</section>

<section class="abs hotels">
  <h2 class="heading abs" style="top:55px;width:1200px;font-size:26px;color:#fff">HOTELS</h2>
  <div class="subtabs abs" style="top:100px;width:1200px;color:#fff"><span>LUXURY HOTELS</span><i>|</i><span>CHEAP HOTELS</span><i>|</i><span>POPULAR HOTELS</span></div>

  <svg class="abs" style="left:84px;top:236px" width="18" height="30" viewBox="0 0 18 30"><path d="M15 2 3 15l12 13" fill="none" stroke="#fff" stroke-width="3"/></svg>
  <svg class="abs" style="left:1096px;top:236px" width="18" height="30" viewBox="0 0 18 30"><path d="m3 2 12 13L3 28" fill="none" stroke="#fff" stroke-width="3"/></svg>

  <div class="hotel-img" style="left:143px;background:linear-gradient(160deg,#5a9ee0,#7b8799 50%,#8a5a3f)" role="img" aria-label="Photo of London tower blocks"></div>
  <div class="hotel-img" style="left:454px;background:linear-gradient(160deg,#6aa5e0,#b9b2a5 50%,#6d6457)" role="img" aria-label="Photo of a Paris stone building facade"></div>
  <div class="hotel-img" style="left:767px;background:linear-gradient(160deg,#3a6fb8,#2c4a7a 50%,#26344f)" role="img" aria-label="Photo of Berlin glass towers at dusk"></div>

  <div class="hotel-info" style="left:143px"><b>London, UK</b><span>Fantacy Serviced Apartments</span><i>★★★★★</i></div>
  <div class="hotel-info" style="left:454px"><b>Paris, France</b><span>Fantacy Serviced Apartments</span><i>★★★★★</i></div>
  <div class="hotel-info" style="left:767px"><b>Berlin, Germany</b><span>Fantacy Serviced Apartments</span><i>★★★★★</i></div>
</section>

<section class="abs forum">
  <h2 class="heading abs" style="top:58px;width:1200px;font-size:24px">LATEST TRAVEL FORUM</h2>
  <p class="tagline abs" style="top:91px;width:1200px">PLEASE SHARE YOUR EXPERIENCE HERE</p>

  <div class="abs table">
    <div class="thead"><span class="c1">TITLE</span><span class="c2">POSTED ON</span><span class="c3">VIEWS / REPLIES</span></div>
    <div class="row"><div class="c1"><b>Why Hawaii is a hub for entertainment?</b><small>By : Tobias Renner</small></div><div class="c2">15 Jan 2017, 07:45 AM</div><div class="c3">View : <em>1450</em><br>Replies : <em>45</em></div></div>
    <div class="row"><div class="c1"><b>Whis the hottest place in January?</b><small>By : Milan Draskov</small></div><div class="c2">15 Jan 2017, 06:45 AM</div><div class="c3">View : <em>1950</em><br>Replies : <em>75</em></div></div>
    <div class="row"><div class="c1"><b>Must visit destinations in the world which make you feel better...</b><small>By : Milan Draskov</small></div><div class="c2">15 Jan 2017, 06:45 AM</div><div class="c3">View : <em>1950</em><br>Replies : <em>75</em></div></div>
    <div class="row"><div class="c1"><b>Why Hawaii is a hub for entertainment?</b><small>By : Tobias Renner</small></div><div class="c2">15 Jan 2017, 07:45 AM</div><div class="c3">View : <em>1450</em><br>Replies : <em>45</em></div></div>
    <div class="row"><div class="c1"><b>Whis the hottest place in January?</b><small>By : Milan Draskov</small></div><div class="c2">15 Jan 2017, 06:45 AM</div><div class="c3">View : <em>1950</em><br>Replies : <em>75</em></div></div>
  </div>

  <div class="btn" style="left:551px;top:529px;width:95px;height:31px;line-height:31px">VIEW ALL</div>
</section>

<section class="abs newsletter">
  <h2 class="heading abs" style="top:42px;width:1200px">SIGN UP TO OUR NEWSLETTER</h2>
  <p class="sub abs" style="top:68px;width:1200px">GET UPDATED FOR SPECIAL OFFERS</p>
  <div class="abs email"><svg width="14" height="10" viewBox="0 0 14 10"><rect width="14" height="10" fill="var(--gold)"/><path d="m0 0 7 5 7-5" fill="none" stroke="#fff"/></svg>Enter your email address</div>
  <div class="abs submit">SUBMIT</div>
</section>

<section class="abs links">
  <h2 class="heading abs" style="top:55px;width:1200px;font-size:24px">POPULAR LINKS YOU MAY INTERESTED</h2>
  <svg width="0" height="0" style="position:absolute"><defs><symbol id="tick" viewBox="0 0 14 11"><path d="m1 5.5 4 4L13 1" fill="none" stroke="#b59a5a" stroke-width="2.2"/></symbol></defs></svg>

  <div class="link" style="left:143px;top:120px"><svg width="14" height="11"><use href="#tick"/></svg>New York Holidays</div>
  <div class="link" style="left:454px;top:120px"><svg width="14" height="11"><use href="#tick"/></svg>Amsterdam Hotels</div>
  <div class="link" style="left:767px;top:120px"><svg width="14" height="11"><use href="#tick"/></svg>Dubai Holidays</div>

  <div class="link" style="left:143px;top:180px"><svg width="14" height="11"><use href="#tick"/></svg>UK Car Hire</div>
  <div class="link" style="left:454px;top:180px"><svg width="14" height="11"><use href="#tick"/></svg>Oralando Flights</div>
  <div class="link" style="left:767px;top:180px"><svg width="14" height="11"><use href="#tick"/></svg>Bangkok Flights</div>

  <div class="link" style="left:143px;top:240px"><svg width="14" height="11"><use href="#tick"/></svg>Sydney Flights</div>
  <div class="link" style="left:454px;top:240px"><svg width="14" height="11"><use href="#tick"/></svg>Hawaii Hotels</div>
  <div class="link" style="left:767px;top:240px"><svg width="14" height="11"><use href="#tick"/></svg>Paris Car Hire</div>

  <div class="link" style="left:143px;top:300px"><svg width="14" height="11"><use href="#tick"/></svg>New York Holidays</div>
  <div class="link" style="left:454px;top:300px"><svg width="14" height="11"><use href="#tick"/></svg>Amsterdam Hotels</div>
  <div class="link" style="left:767px;top:300px"><svg width="14" height="11"><use href="#tick"/></svg>Dubai Holidays</div>

  <div class="link" style="left:143px;top:360px"><svg width="14" height="11"><use href="#tick"/></svg>UK Car Hire</div>
  <div class="link" style="left:454px;top:360px"><svg width="14" height="11"><use href="#tick"/></svg>Oralando Flights</div>
  <div class="link" style="left:767px;top:360px"><svg width="14" height="11"><use href="#tick"/></svg>Bangkok Flights</div>
</section>

<footer class="abs footer" role="img" aria-label="City skyline silhouette over water with a plane trail arcing across the sky">
  <span class="brand">Mirdalon</span>
  <div class="socials"><span></span><span></span><span></span></div>
  <nav><span>HOME</span><span>ABOUT US</span><span>CUSTOMER SUPPORT</span><span>PRIVACY</span><span>TERMS OF USE</span></nav>
  <p class="copy">© 2016 MIRDALON. ALL RIGHTS RESERVED.</p>
</footer>

</body>
</html>
```